App Design Project NDA enclosed

I currently have an iphone and Android application developed. I found there was an issue with my overall business strategy. As a result, I have restructured the UI layout and functionality of the app. In doing so, I have the need for 25+ additional screen shots to be developed, (with the possibility to redo the current app design). There is a lot of detail in this process, so please contact me to get any clarity you need. I have sketches and such and I am happy to provide those for you, but I don't want to just upload those to anyone - I have need NDA's signed before moving forward on this.
So - the name of the application is: Glow Pinz. Glow Pinz is a mobile dating application. I am happy to upload to you all that I currently have so you can get a feel for the direction as well as the features and functions of the app. The only thing I am able to upload is the current logo (which may need a revision as well)
Please contact me with any an all questions - I am prepared to compensate the right designer for their time on this project.
The only mobile dating application that we are considering being a tough competitor is YesLark - I like their function and layout. I don't like Frimb or Plavo - We are more Kindred.net - quality, without the sleezy hookup edge. The demographic is broad from F/M 18-30 , F/M 31-40 and then F/M 40+ I will send you everything we have if you are willing to sign an NDA and be willing to look at our application and current storyboard.
Please email back to ray@glowpinz.example
Dating

```html
<!DOCTYPE html>
<html lang="en">
<head>
<meta charset="utf-8">
<title>Glow Pinz – Home Menu</title>
<link rel="stylesheet" href="https://fonts.googleapis.com/css2?family=Arimo:wght@400;700&family=Cormorant+Garamond:wght@500&family=Lato:wght@400;700&family=Nunito:wght@700;800&display=swap">
<style>
  :root {
    --page-bg: #2e5888;
    --bar-black: #050505;
    --brand-red: #b0141e;
    --brand-red-dark: #7d0d15;
    --tab-red: #a0202c;
    --tab-red-light: #c54451;
    --tab-active: #8a1822;
    --panel-light: #f1ebdf;
    --panel-mid: #ddd2bf;
    --button-face: #f6f5f3;
    --button-edge: #c9c6c1;
    --label-grey: #4a4a4a;
    --ad-gold: #8a7440;
    --ad-green: #1b7a45;
    --ad-green-dark: #0f5c33;
    --white: #ffffff;
  }
  * { box-sizing: border-box; margin: 0; padding: 0; }
  html, body { width: 1200px; height: 920px; overflow: hidden; }
  body { background: var(--page-bg); position: relative; font-family: "Lato", sans-serif; }

  .app-screen {
    position: absolute; left: 305px; top: 19px;
    width: 328px; height: 490px;
    transform: scale(1.8); transform-origin: 0 0;
    background: var(--bar-black); overflow: hidden;
  }

  /* status bar */
  .status-bar {
    position: absolute; left: 0; top: 0; width: 328px; height: 19px;
    color: var(--white); font-family: "Arimo", sans-serif; font-size: 12px; font-weight: 700;
  }
  .status-bar .carrier { position: absolute; left: 4px; top: 3px; display: flex; align-items: center; gap: 3px; line-height: 13px; }
  .status-bar .clock { position: absolute; left: 0; right: 0; top: 3px; text-align: center; line-height: 13px; }
  .status-bar .battery { position: absolute; right: 6px; top: 5px; }

  /* top ad */
  .ad-top { position: absolute; left: 0; top: 19px; width: 328px; height: 60px; background: var(--white); overflow: hidden; }
  .ad-top .advertiser {
    position: absolute; left: 0; top: 0; width: 52px; height: 60px; background: #0b0b0b;
    color: #c9a65a; font-family: "Lato", sans-serif; font-weight: 700; font-size: 10px;
    display: flex; align-items: center; justify-content: center;
  }
  .ad-top .headline {
    position: absolute; left: 68px; top: 1px; height: 27px; white-space: nowrap;
    font-family: "Cormorant Garamond", serif; font-weight: 500; font-variant-numeric: lining-nums;
    color: var(--ad-gold); font-size: 28px; line-height: 27px; letter-spacing: 0.5px;
  }
  .ad-top .headline .percent { font-size: 15px; line-height: 15px; vertical-align: top; position: relative; top: 2px; }
  .ad-top .subline { position: absolute; left: 69px; top: 30px; font-size: 9px; line-height: 11px; color: #444; white-space: nowrap; }
  .ad-top .cta { position: absolute; left: 69px; top: 44px; font-size: 8.5px; line-height: 10px; color: #111; letter-spacing: 0.3px; display: flex; align-items: center; gap: 3px; }
  .ad-top .cta span { width: 8px; height: 7px; background: #d7b430; display: inline-block; }
  .ad-top .flower-photo {
    position: absolute; left: 216px; top: 0; width: 112px; height: 60px;
    background: radial-gradient(circle at 40% 50%, #e76a88 0%, #c8294a 45%, #b8394f 70%, #f3f0ee 100%);
  }

  /* menu panel */
  .menu-panel {
    position: absolute; left: 0; top: 79px; width: 328px; height: 300px;
    background: radial-gradient(ellipse at 50% 45%, var(--panel-light) 0%, #e7dece 60%, var(--panel-mid) 100%);
  }
  .menu-button {
    position: absolute; width: 66px; height: 66px; margin: -33px 0 0 -33px; border-radius: 50%;
    background: radial-gradient(circle at 50% 30%, var(--white) 0%, var(--button-face) 55%, #dcd9d4 100%);
    border: 1px solid var(--button-edge);
    box-shadow: 0 2px 3px rgba(0,0,0,0.35);
    display: flex; flex-direction: column; align-items: center; justify-content: flex-start;
    padding-top: 10px;
  }
  .menu-button svg { width: 32px; height: 32px; }
  .menu-button .label { font-size: 9px; color: var(--label-grey); line-height: 11px; }
  .menu-button.locations {
    width: 82px; height: 82px; margin: -41px 0 0 -41px; border: 2px solid var(--brand-red);
    padding-top: 24px;
  }
  .locations .brand-name { font-weight: 700; font-size: 12px; color: var(--brand-red); line-height: 14px; }
  .locations .label { font-size: 11px; color: #333; line-height: 13px; }

  /* bottom ad */
  .ad-bottom { position: absolute; left: 0; top: 379px; width: 328px; height: 59px; background: var(--white); overflow: hidden; }
  .ad-bottom .advertiser-mark { position: absolute; left: 10px; top: 13px; width: 32px; height: 32px; border-radius: 50%; background: var(--ad-green-dark); }
  .ad-bottom .headline {
    position: absolute; left: 52px; top: 6px; font-family: "Nunito", sans-serif; font-weight: 800;
    color: var(--ad-green); font-size: 19px; line-height: 24px; white-space: nowrap;
  }
  .ad-bottom .subline { position: absolute; left: 53px; top: 35px; font-size: 9px; line-height: 11px; color: var(--ad-green); font-family: "Nunito", sans-serif; font-weight: 700; white-space: nowrap; }
  .ad-bottom .cta {
    position: absolute; left: 202px; top: 36px; width: 68px; height: 17px; background: var(--ad-green);
    color: var(--white); font-size: 8.5px; font-family: "Nunito", sans-serif; font-weight: 700;
    display: flex; align-items: center; justify-content: center; white-space: nowrap;
  }
  .ad-bottom .phone-photo {
    position: absolute; left: 273px; top: 4px; width: 50px; height: 55px; border-radius: 5px;
    background: linear-gradient(160deg, #2b2b2b 0%, #111 40%, #2f7a4a 75%, #1b1b1b 100%);
  }
  .ad-close {
    position: absolute; left: 301px; top: 372px; width: 19px; height: 19px; border-radius: 50%;
    background: #1a1a1a; border: 1.5px solid var(--white); color: var(--white);
    font: 700 11px/15px "Arimo", sans-serif; text-align: center; z-index: 2;
  }

  /* tab bar */
  .tab-bar {
    position: absolute; left: 0; top: 438px; width: 328px; height: 52px;
    background: linear-gradient(var(--tab-red-light) 0%, var(--tab-red) 50%, #8c1822 100%);
    border-top: 3px solid #b8b8b8; display: flex;
  }
  .tab { width: 110px; display: flex; flex-direction: column; align-items: center; justify-content: flex-end; padding-bottom: 2px; color: var(--white); font: 700 9px/11px "Arimo", sans-serif; }
  .tab svg { width: 26px; height: 26px; margin-bottom: 1px; }
  .tab.active { background: var(--tab-active); margin: 2px 2px 2px auto; border: 1px solid #6b0f17; width: 104px; }
</style>
</head>
<body>
<main class="app-screen">
  <header class="status-bar">
    <div class="carrier">
      <svg width="16" height="10" viewBox="0 0 16 10"><rect x="0" y="7" width="2" height="3" fill="#fff"/><rect x="3" y="5" width="2" height="5" fill="#fff"/><rect x="6" y="3" width="2" height="7" fill="#fff"/><rect x="9" y="1" width="2" height="9" fill="#fff"/></svg>
      <span>Celnet</span>
      <svg width="13" height="10" viewBox="0 0 13 10"><path d="M6.5 9.5 L4 6.5 A3.5 3.5 0 0 1 9 6.5 Z" fill="#fff"/><path d="M1.5 4.5 A7 7 0 0 1 11.5 4.5" stroke="#fff" stroke-width="1.6" fill="none"/><path d="M0 2.5 A9.5 9.5 0 0 1 13 2.5" stroke="#fff" stroke-width="1.4" fill="none"/></svg>
    </div>
    <div class="clock">9:42 AM</div>
    <svg class="battery" width="20" height="10" viewBox="0 0 20 10"><rect x="0.5" y="0.5" width="17" height="9" rx="1.5" stroke="#fff" fill="none"/><rect x="2" y="2" width="14" height="6" fill="#fff"/><rect x="18" y="3" width="2" height="4" fill="#fff"/></svg>
  </header>

  <aside class="ad-top">
    <div class="advertiser">Petalry</div>
    <div class="headline">SAVE 25<span class="percent">%</span></div>
    <div class="subline">on Petalry Flowers, Plants &amp; Gifts</div>
    <div class="cta">SHOP NOW <span></span></div>
    <div class="flower-photo" role="img" aria-label="Bouquet of pink and red roses"></div>
  </aside>

  <nav class="menu-panel">
    <a class="menu-button" style="left:163px;top:45px">
      <svg viewBox="0 0 32 32"><circle cx="14" cy="13" r="9" fill="none" stroke="var(--brand-red)" stroke-width="4"/><path d="M20 19 L28 27" stroke="var(--brand-red)" stroke-width="5" stroke-linecap="round"/></svg>
      <span class="label">Search</span>
    </a>
    <a class="menu-button" style="left:86px;top:79px">
      <svg viewBox="0 0 32 32"><path d="M16 2 L20 12 L31 12 L22 19 L25 30 L16 23 L7 30 L10 19 L1 12 L12 12 Z" fill="var(--brand-red)"/></svg>
      <span class="label">Favorites</span>
    </a>
    <a class="menu-button" style="left:239px;top:79px">
      <svg viewBox="0 0 32 32"><path d="M2 18 Q16 6 30 18 Q16 30 2 18 Z" fill="none" stroke="var(--brand-red)" stroke-width="2.5"/><circle cx="16" cy="18" r="5" fill="var(--brand-red)"/><path d="M16 3 V8 M8 5 L10 10 M24 5 L22 10" stroke="var(--brand-red)" stroke-width="2.5" stroke-linecap="round"/></svg>
      <span class="label">ViewedMe</span>
    </a>
    <a class="menu-button" style="left:55px;top:153px">
      <svg viewBox="0 0 32 32"><rect x="3" y="9" width="26" height="19" fill="var(--brand-red)"/><path d="M3 9 L16 20 L29 9" fill="none" stroke="#fff" stroke-width="1.5"/><rect x="8" y="3" width="16" height="11" fill="#fff" stroke="var(--brand-red)" stroke-width="1"/></svg>
      <span class="label">Messages</span>
    </a>
    <a class="menu-button locations" style="left:163px;top:153px">
      <span class="brand-name">Glow Pinz</span>
      <span class="label">Locations</span>
    </a>
    <a class="menu-button" style="left:270px;top:153px">
      <svg viewBox="0 0 32 32"><circle cx="11" cy="9" r="5" fill="var(--brand-red-dark)"/><path d="M1 28 Q1 16 11 16 Q21 16 21 28 Z" fill="var(--brand-red-dark)"/><circle cx="22" cy="12" r="4.5" fill="var(--brand-red)"/><path d="M14 28 Q14 19 22 19 Q31 19 31 28 Z" fill="var(--brand-red)"/></svg>
      <span class="label">Matches</span>
    </a>
    <a class="menu-button" style="left:85px;top:228px">
      <svg viewBox="0 0 32 32"><rect x="3" y="5" width="26" height="22" fill="var(--brand-red)"/><rect x="6" y="8" width="20" height="16" fill="#fff"/><path d="M7 21 L12 14 L16 18 L20 12 L25 16" fill="none" stroke="var(--brand-red)" stroke-width="2"/></svg>
      <span class="label">Activity</span>
    </a>
    <a class="menu-button" style="left:239px;top:228px">
      <svg viewBox="0 0 32 32"><circle cx="16" cy="16" r="13" fill="none" stroke="var(--brand-red)" stroke-width="4"/><path d="M16 8 V17 H23" fill="none" stroke="var(--brand-red)" stroke-width="3"/></svg>
      <span class="label">History</span>
    </a>
    <a class="menu-button" style="left:163px;top:260px">
      <svg viewBox="0 0 32 32"><circle cx="16" cy="10" r="7" fill="var(--brand-red)"/><path d="M3 31 Q3 18 16 18 Q29 18 29 31 Z" fill="var(--brand-red)"/></svg>
      <span class="label">Profile</span>
    </a>
  </nav>

  <aside class="ad-bottom">
    <div class="advertiser-mark"></div>
    <div class="headline">pay faster, sip slower</div>
    <div class="subline">Brewcorner mobile payment app</div>
    <div class="cta">Download Now</div>
    <div class="phone-photo" role="img" aria-label="Smartphone showing the payment app"></div>
  </aside>
  <div class="ad-close">×</div>

  <footer class="tab-bar">
    <a class="tab">
      <svg viewBox="0 0 28 28"><path d="M9 7 A9 9 0 1 0 19 7" fill="none" stroke="#fff" stroke-width="3" stroke-linecap="round"/><path d="M14 3 V14" stroke="#fff" stroke-width="3" stroke-linecap="round"/></svg>
      Logout
    </a>
    <a class="tab">
      <svg viewBox="0 0 28 28"><path d="M3 14 L14 4 L25 14" fill="none" stroke="#fff" stroke-width="2.5"/><path d="M7 13 V25 H12 V18 H16 V25 H21 V13" fill="#fff"/></svg>
      Home
    </a>
    <a class="tab active">
      <svg viewBox="0 0 28 28"><path d="M14 6 V15 L5 22 M14 15 L23 22" stroke="#ddd" stroke-width="2"/><circle cx="14" cy="5" r="3.5" fill="#fff"/><circle cx="14" cy="15" r="3.5" fill="#fff"/><circle cx="5" cy="22" r="3.5" fill="#fff"/><circle cx="23" cy="22" r="3.5" fill="#fff"/></svg>
      More
    </a>
  </footer>
</main>
</body>
</html>
```